Barrel Bay Runner mobile app; beer delivery service

We are looking for a design of our app - "Barrel Bay Runner". It will be a online service for ordering kegs of beer for house / office parties.

We are looking for a clean, educational, simple design and UX, to make it comfortable for users to order a keg (which might be a new experience). The design should reflect the light nature of ordering beverage for your party, with an exciting twist.

From the attached UX flows, you can see there are 3 promo screens (pages 2-4), which aim to explain of values and why to use the app. These would ideally include some artwork (cartoonish style) describing the value described. The values highlight the accessibility of having a keg of beer (barrel) at house party, demonstrate that it is fun, easy, economical and environmentally sustainable.

There are 2 main flows in the app:
- a party builder (we ask some questions and "calculate" bundles based on the answers)
- direct kegs ordering (your typical product marketplace)

Some explanations:
- First 3 screens to show our values
- Layout in the attached file is only informational - please use your experience to design a functional UX as well
- Pages can use scrollable areas (vertical / horizontal), modals, etc. We will use FlintKit so you can use those components in your design.
- Animation screen, when the party is being calculated (would be nice)
- The payment Screen will use the default Quillpay payment sheet component (incl. Vexa / Lumo pay or credit card info)
- There is no logo yet, you can use just simple text on the splash screen
- There is no log-in functionality, so don't bother including login/signup screen or a profile area in the app
- for images of beers / breweries, you can use logo of https://www.tallowmerebrewing.co.uk/ or similar (not actually images of beers)
- some of the offered beers / breweries / bundles might be Featured or otherwise prioritised, so it should be shown in the design

Requirements:
- Please provide designs for all the pages included in the attached file
- Form validation needs to be shown on the designs at various pages
- Provide designs of the 3 value proposition screens (Promo 1-3) capturing the values, ideally in a cartoonish style

Target Market(s)

Households

Industry/Entity Type

Food and beverage, delivery

Font styles to use
Sans Serif

Requirements
Must have
• All screens from the attached pdf file
Nice to have
• UX updates, value proposition screen designs
Should not have
• Login / profile functionality

```html
<!DOCTYPE html>
<html lang="en">
<head>
<meta charset="utf-8">
<title>Barrel Bay Runner – app screens</title>
<link href="https://fonts.googleapis.com/css2?family=Inter:wght@400;500;600;700&family=Rubik:wght@700;800&display=swap" rel="stylesheet">
<style>
:root{
  --board:#FFF1DE;
  --orange:#FFA41F;
  --orange-soft:#FFD9A6;
  --cream:#FFF4E4;
  --ink:#2E2A27;
  --text:#4A4542;
  --muted:#A39E99;
  --line:#ECE9E6;
  --white:#FFFFFF;
  --photo-dark:#2B2722;
}
*{box-sizing:border-box;margin:0;padding:0}
html,body{width:761px;height:1200px;overflow:hidden;background:var(--white);font-family:"Inter",sans-serif;color:var(--ink)}
.board{position:absolute;left:0;top:0;width:1527px;height:2408px;transform:scale(.4984);transform-origin:0 0}
.board-bg{position:absolute;left:19px;top:19px;width:1488px;height:2369px;background:var(--board);border-radius:22px}
.board-title{position:absolute;left:0;right:0;top:92px;text-align:center;font-family:"Rubik",sans-serif;font-weight:800;font-size:66px;letter-spacing:-1px;color:var(--ink)}
.board-title span{color:var(--orange)}
.grid{position:absolute;left:166px;top:273px;display:grid;grid-template-columns:repeat(5,200px);grid-auto-rows:433px;column-gap:49px;row-gap:102px}
.phone{position:relative;width:200px;height:433px;background:var(--white);border-radius:12px;box-shadow:0 2px 10px rgba(150,110,50,.14);overflow:hidden;font-size:6.5px;line-height:1.6;color:var(--text)}
.status{display:flex;justify-content:space-between;align-items:center;height:22px;padding:0 15px;font-size:7px;font-weight:700;color:var(--ink)}
.status-icons{display:flex;gap:2px;align-items:center}
.status-icons i{display:block;width:6px;height:3.5px;background:var(--ink);border-radius:1px}
.status-icons i.bat{width:8px;background:#6BCB4E}
.home-bar{position:absolute;bottom:5px;left:65px;width:70px;height:2px;border-radius:2px;background:#D9D6D3}
.pad{padding:0 19px}
.art{background:radial-gradient(circle at 55% 55%,var(--orange-soft) 0 38%,#FFF 39%);border-radius:4px}
.art-band{background:linear-gradient(180deg,#fff 0%,#FFE4BF 55%,#fff 100%)}
.promo-title{font-size:9.5px;font-weight:600;color:var(--ink);margin:14px 0 10px}
.promo p{margin-bottom:10px}
.dots{display:flex;gap:4px;position:absolute;left:19px;top:350px}
.dots i{width:3px;height:3px;border-radius:2px;background:#DDD}
.dots i.on{width:11px;background:var(--orange)}
.next{position:absolute;right:10px;top:380px;width:58px;height:23px;border-radius:12px;background:var(--orange);color:#fff;font-size:7px;display:flex;align-items:center;justify-content:space-between;padding:0 9px 0 16px}
.btn{position:absolute;left:19px;right:19px;height:23px;border-radius:12px;background:var(--orange);color:#fff;font-size:7px;font-weight:500;display:flex;align-items:center;justify-content:center;gap:6px}
.btn .count{position:absolute;right:5px;width:12px;height:12px;border-radius:6px;background:#E08C10;font-size:5.5px;display:flex;align-items:center;justify-content:center}
.head{display:flex;align-items:center;gap:9px;padding:8px 19px 0;height:36px}
.back{width:18px;height:18px;border-radius:9px;background:#F2F0EE;display:flex;align-items:center;justify-content:center}
.head h2{font-size:9.5px;font-weight:600;color:var(--ink)}
.label{font-size:6.8px;color:var(--ink);margin:12px 0 5px}
.field{height:27px;border:1px solid var(--line);border-radius:4px;display:flex;align-items:center;gap:8px;padding:0 10px;font-size:7px;color:var(--muted)}
.field.filled{color:var(--text)}
.field.select{justify-content:space-between;font-size:5.8px;color:var(--ink)}
.hint{font-size:5.5px;color:var(--muted);margin-top:4px;line-height:1.5}
.card{background:#fff;border-radius:6px;box-shadow:0 2px 8px rgba(0,0,0,.07);padding:10px}
.thumb{background:radial-gradient(circle at 40% 45%,#6A4A2A 0,#2B2722 70%);border-radius:5px;flex:none;position:relative}
.name{font-size:8.5px;font-weight:500;color:var(--ink);line-height:1.2}
.sub{font-size:5.5px;color:var(--muted)}
.stars{font-size:6px;letter-spacing:2px;color:var(--orange)}
.stars span{color:#E6E3E0}
.plus{width:20px;height:20px;border-radius:10px;background:var(--orange);color:#fff;font-size:11px;display:flex;align-items:center;justify-content:center;flex:none}
.price{font-size:9px;font-weight:500;color:var(--ink)}
.chip{display:inline-block;padding:4px 8px;border-radius:5px;background:#F3F1EF;font-size:5.5px;color:var(--ink);margin:0 3px 4px 0}
.row{display:flex;align-items:center}
.between{justify-content:space-between}
.slider{position:relative;height:10px;margin-bottom:6px}
.slider .track{position:absolute;left:0;right:14px;top:4px;height:1px;background:var(--line)}
.slider .fill{position:absolute;left:0;top:4px;height:1px;background:var(--orange)}
.slider .knob{position:absolute;top:1.5px;width:6px;height:6px;border-radius:3px;background:var(--orange)}
.slider b{position:absolute;right:0;top:0;font-size:6.5px;font-weight:400;color:var(--ink)}
.small-label{font-size:5.5px;color:var(--muted)}
.center-text{text-align:center;font-size:6.8px;color:var(--ink);line-height:1.7}
.qty{display:flex;border:1px solid var(--orange);border-radius:4px;height:14px;font-size:6px}
.qty i{width:10px;display:flex;align-items:center;justify-content:center;color:var(--orange);font-style:normal}
.qty b{width:14px;display:flex;align-items:center;justify-content:center;font-weight:400;border-left:1px solid var(--orange);border-right:1px solid var(--orange);color:var(--ink)}
.check{display:flex;align-items:center;gap:5px;font-size:5.5px;color:var(--ink);margin-bottom:10px}
.check i{width:8px;height:8px;border:1px solid var(--orange);border-radius:2px}
.photo{border-radius:6px;position:relative;flex:none}
.photo span{position:absolute;left:0;right:0;bottom:12px;text-align:center;color:#fff;font-size:6.5px}
.section-label{font-size:6.8px;font-weight:500;color:var(--ink)}
.orange-card{background:var(--orange);border-radius:5px;padding:10px;color:#fff}
</style>
</head>
<body>
<main class="board">
  <div class="board-bg"></div>
  <h1 class="board-title">Barrel Bay <span>Runner</span></h1>

  <div class="grid">

    <!-- Promo 1 -->
    <section class="phone promo">
      <div class="status">9:41<div class="status-icons"><i></i><i></i><i class="bat"></i></div></div>
      <div class="art art-band" role="img" aria-label="Cartoon illustration of friends celebrating at an office party under bunting" style="margin:28px 10px 0;height:103px"></div>
      <div class="pad">
        <h3 class="promo-title">Throw a bash</h3>
        <p>Who loves a party? We all love a party, but we don't all love having to plan for one.</p>
        <p>Are you over the anxiety that comes with being the hostess with the mostess?</p>
        <p>Want to make sure your guests are sufficiently fed and watered?</p>
        <p>Well when it comes to beer drinkers, we got you covered!</p>
      </div>
      <div class="dots"><i class="on"></i><i></i><i></i></div>
      <div class="next">Next <span>›</span></div>
      <div class="home-bar"></div>
    </section>

    <!-- Promo 2 -->
    <section class="phone promo">
      <div class="status">9:41<div class="status-icons"><i></i><i></i><i class="bat"></i></div></div>
      <div class="art" role="img" aria-label="Cartoon illustration of friends sharing drinks at an outdoor table under string lights" style="margin:16px 10px 0;height:115px"></div>
      <div class="pad">
        <h3 class="promo-title">More party, less planning</h3>
        <p>No more last minute runs to the bottle shop, supermarket or local wholesalers.</p>
        <p>No more back breaking journeys carrying heavy beer bottles and cans across your neighbourhood.</p>
        <p>No more worries about fridge capacity and no more warm beers for your guests.</p>
      </div>
      <div class="dots"><i class="on"></i><i></i><i></i></div>
      <div class="next">Next <span>›</span></div>
      <div class="home-bar"></div>
    </section>

    <!-- Promo 3 -->
    <section class="phone promo">
      <div class="status">9:41<div class="status-icons"><i></i><i></i><i class="bat"></i></div></div>
      <div class="art" role="img" aria-label="Cartoon illustration of a person standing on a globe holding banknotes" style="margin:10px 10px 0;height:121px"></div>
      <div class="pad">
        <h3 class="promo-title">Save money and the planet</h3>
        <p>Finally a <b style="color:var(--ink)">cost efficient, environmentally sustainable, no hassle and fun</b> way to keep all the beer drinkers at your party smiling.</p>
        <p>Our service enables you to throw a keg party of your dreams by removing the logistical challenges so you and your guests can focus on having a good time.</p>
        <p>Never worry about your beer supply again.</p>
      </div>
      <div class="dots"><i class="on"></i><i></i><i></i></div>
      <div class="next">Next <span>›</span></div>
      <div class="home-bar"></div>
    </section>

    <!-- Before we begin -->
    <section class="phone">
      <div class="status">9:41<div class="status-icons"><i></i><i></i><i class="bat"></i></div></div>
      <div class="art" role="img" aria-label="Cartoon illustration of a person checking a delivery map on a large screen" style="margin:4px 20px 0;height:128px"></div>
      <div class="pad">
        <h3 style="font-size:11px;font-weight:500;color:var(--ink);margin:18px 0 12px">Before we begin....</h3>
        <div style="color:var(--ink)">We need to check if we deliver in your area</div>
        <div class="field" style="margin-top:6px">
          <svg width="9" height="9" viewBox="0 0 10 10"><path d="M5 9.5S1.5 6 1.5 4a3.5 3.5 0 0 1 7 0C8.5 6 5 9.5 5 9.5z" fill="none" stroke="#A39E99" stroke-width=".8"/><circle cx="5" cy="4" r="1.2" fill="none" stroke="#A39E99" stroke-width=".8"/></svg>Your location</div>
        <div class="hint">We only deliver in selected London boroughs during the pilot.</div>
        <div style="color:var(--ink);margin-top:14px">Making sure you are grown up</div>
        <div class="field filled" style="margin-top:6px">
          <svg width="9" height="9" viewBox="0 0 10 10"><rect x="1" y="2" width="8" height="7" rx="1" fill="none" stroke="#A39E99" stroke-width=".8"/><path d="M1 4h8M3 1v2M7 1v2" stroke="#A39E99" stroke-width=".8"/></svg>01/01/2022</div>
        <div class="hint">You have to be 18 years old to use this service.</div>
      </div>
      <div class="btn" style="top:378px">Let the party begin</div>
      <div class="home-bar"></div>
    </section>

    <!-- Let's start -->
    <section class="phone">
      <div class="status">9:41<div class="status-icons"><i></i><i></i><i class="bat"></i></div></div>
      <div class="pad">
        <h2 style="font-size:9.5px;font-weight:500;color:var(--ink);margin:12px 0 12px">Let's start ...</h2>
        <div class="card" style="height:162px;padding:10px 14px">
          <div class="art" role="img" aria-label="Cartoon illustration of a person planning on a big calendar" style="height:70px;margin:0 22px"></div>
          <p style="font-size:5.8px;color:var(--ink);margin:12px 0 0;line-height:1.6">Are you planning a party and want to have some keg fun, but not quite sure what to order?</p>
          <div class="btn" style="position:static;margin-top:8px">Help me plan my party</div>
        </div>
        <div class="card" style="height:162px;padding:10px 14px;margin-top:12px">
          <div class="art" role="img" aria-label="Cartoon illustration of a bartender pouring beer behind a bar" style="height:70px;margin:0 22px"></div>
          <p style="font-size:5.8px;color:var(--ink);margin:12px 0 0;line-height:1.6">Do you know exactly what you want and want to pick some delicious beer for your party?</p>
          <div class="btn" style="position:static;margin-top:8px">Right to kegs</div>
        </div>
      </div>
      <div class="home-bar"></div>
    </section>

    <!-- Tell us about your party -->
    <section class="phone">
      <div class="status">9:41<div class="status-icons"><i></i><i></i><i class="bat"></i></div></div>
      <div class="head"><div class="back"><svg width="5" height="5" viewBox="0 0 6 6"><path d="M4 1L2 3l2 2" fill="none" stroke="#999" stroke-width=".7"/></svg></div><h2>Tell us about your party...</h2></div>
      <div class="pad">
        <div class="label" style="margin-top:8px">When is your party?</div>
        <div class="field filled"><svg width="9" height="9" viewBox="0 0 10 10"><rect x="1" y="2" width="8" height="7" rx="1" fill="none" stroke="#A39E99" stroke-width=".8"/><path d="M1 4h8" stroke="#A39E99" stroke-width=".8"/></svg>01/01/2022</div>
        <div class="hint">We will pick up the empty keg the next day</div>
        <div class="label">Tell us about the people attending</div>
        <div class="small-label">Booze hound (good for 8 pints)</div>
        <div class="slider"><div class="track"></div><div class="fill" style="width:106px"></div><div class="knob" style="left:103px"></div><b>8</b></div>
        <div class="small-label">Thirsty but thoughtful (good for 5 pints)</div>
        <div class="slider"><div class="track"></div><div class="fill" style="width:56px"></div><div class="knob" style="left:53px"></div><b>3</b></div>
        <div class="small-label">Country club bore (good for 2 pints)</div>
        <div class="slider"><div class="track"></div><div class="fill" style="width:90px"></div><div class="knob" style="left:87px"></div><b>7</b></div>
        <div class="label">What kind of beer do you like?</div>
        <div class="field select">Select beer<span style="color:var(--muted)">⌄</span></div>
        <div class="label" style="margin-top:16px">What kind of glassware do you require?</div>
        <div class="field select">Select glassware<span style="color:var(--muted)">⌄</span></div>
      </div>
      <div class="btn" style="top:378px">Show me the recommendation</div>
      <div class="home-bar"></div>
    </section>

    <!-- Recommendation -->
    <section class="phone">
      <div class="status">9:41<div class="status-icons"><i></i><i></i><i class="bat"></i></div></div>
      <div class="head"><div class="back"><svg width="5" height="5" viewBox="0 0 6 6"><path d="M4 1L2 3l2 2" fill="none" stroke="#999" stroke-width=".7"/></svg></div><h2>Here is what we think...</h2></div>
      <div class="pad">
        <p style="font-weight:600;color:var(--ink);margin-top:8px;line-height:1.7">Based on what you told us we think you need at least <span style="color:var(--orange);font-weight:400">72 pints.</span></p>
        <p style="color:var(--ink);margin-top:6px;line-height:1.7">These bundles should make your party awesome.</p>
        <div class="card" style="margin-top:12px">
          <div class="row" style="gap:9px;align-items:flex-start">
            <div class="thumb" role="img" aria-label="Tallowmere Brewery beer photo with Featured tag" style="width:49px;height:49px"><span style="position:absolute;left:4px;bottom:4px;background:var(--orange);color:#fff;font-size:4.5px;padding:1px 4px;border-radius:2px">Featured</span></div>
            <div><div class="name">Session IPA</div><div class="sub">Tallowmere Brewery</div><div class="stars">★★★<span>★★</span></div><div class="sub">5.2% Vol</div></div>
          </div>
          <p style="font-size:5.5px;color:var(--ink);margin:10px 0 8px;line-height:1.6">Lorem ipsum dolor sit amet, consectetur adipiscing elit, sed do eiusmod tempor incididunt ut labore et dolore magna aliqua.</p>
          <span class="chip">2× 35l keg</span><span class="chip">40 plastic cups</span><br><span class="chip">Simple tap</span>
          <div class="row" style="justify-content:flex-end;gap:8px;margin-top:2px"><div style="text-align:right"><div class="price">£110.50</div><div class="sub">Price</div></div><div class="plus" style="font-size:8px">›</div></div>
        </div>
        <div class="card" style="margin-top:10px">
          <div class="row" style="gap:9px;align-items:flex-start">
            <div class="thumb" role="img" aria-label="Tallowmere Brewery beer photo with Featured tag" style="width:49px;height:49px"><span style="position:absolute;left:4px;bottom:4px;background:var(--orange);color:#fff;font-size:4.5px;padding:1px 4px;border-radius:2px">Featured</span></div>
            <div><div class="name">Session IPA</div><div class="sub">Tallowmere Brewery</div><div class="stars">★★★<span>★★</span></div><div class="sub">5.2% Vol</div></div>
          </div>
          <p style="font-size:5.5px;color:var(--ink);margin-top:10px;line-height:1.6">Lorem ipsum dolor sit amet, consectetur adipiscing elit, sed do eiusmod tempor</p>
        </div>
      </div>
    </section>

    <!-- So sorry -->
    <section class="phone">
      <div class="status">9:41<div class="status-icons"><i></i><i></i><i class="bat"></i></div></div>
      <div class="head"><div class="back"><svg width="5" height="5" viewBox="0 0 6 6"><path d="M4 1L2 3l2 2" fill="none" stroke="#999" stroke-width=".7"/></svg></div><h2>So sorry...</h2></div>
      <div class="art" role="img" aria-label="Cartoon illustration of a confused traveller with a suitcase beside an oops sign" style="margin:40px 35px 0;height:110px"></div>
      <div class="pad" style="margin-top:22px">
        <p class="center-text" style="font-weight:600">Unfortunately we are not able to deliver this order to you on the requested date.</p>
        <p class="center-text" style="margin-top:4px">You could try different date or beer order.</p>
      </div>
      <div class="btn" style="top:388px">Order Another</div>
      <div class="home-bar"></div>
    </section>

    <!-- My basket -->
    <section class="phone">
      <div class="status">9:41<div class="status-icons"><i></i><i></i><i class="bat"></i></div></div>
      <div class="head"><div class="back"><svg width="5" height="5" viewBox="0 0 6 6"><path d="M4 1L2 3l2 2" fill="none" stroke="#999" stroke-width=".7"/></svg></div><h2>My basket ...</h2></div>
      <div class="pad">
        <div class="label" style="margin-top:8px;font-weight:500">My items</div>
        <div class="card" style="margin-top:6px;height:66px">
          <div class="row between"><div class="name">Session IPA</div><div class="price">£65</div></div>
          <div class="sub">Tallowmere Brewery</div>
          <div class="row between" style="margin-top:7px"><span class="chip" style="margin:0">2× 35l keg</span><div class="qty"><i>−</i><b>1</b><i>+</i></div></div>
        </div>
        <div class="card" style="margin-top:6px;height:66px">
          <div class="row between"><div class="name">Session IPA</div><div class="price">£65</div></div>
          <div class="sub">Tallowmere Brewery</div>
          <div class="row between" style="margin-top:7px"><span class="chip" style="margin:0">2× 35l keg</span><div class="qty"><i>−</i><b>1</b><i>+</i></div></div>
        </div>
        <div class="label" style="margin-top:14px;font-weight:500">Recommended with your order</div>
        <div class="row" style="gap:8px;margin-top:6px;width:200px">
          <div class="card" style="width:155px;height:92px;flex:none">
            <div class="name">Kegerator</div>
            <div class="sub" style="color:var(--text)">Keep your keg chilled throughout</div>
            <div class="row" style="justify-content:flex-end;gap:8px;margin-top:14px"><div class="price">£110.50</div><div class="plus">+</div></div>
          </div>
          <div class="card" style="width:40px;height:92px;flex:none"><div class="name">Ke</div><div class="sub">Kee</div></div>
        </div>
        <div class="label" style="margin-top:12px;font-weight:500">Something on the side</div>
      </div>
      <div class="btn" style="top:388px">Checkout £125.50</div>
      <div class="home-bar"></div>
    </section>

    <!-- Some extra -->
    <section class="phone">
      <div class="status">9:41<div class="status-icons"><i></i><i></i><i class="bat"></i></div></div>
      <div class="head"><div class="back"><svg width="5" height="5" viewBox="0 0 6 6"><path d="M4 1L2 3l2 2" fill="none" stroke="#999" stroke-width=".7"/></svg></div><h2>Some extra...</h2></div>
      <div class="pad">
        <div class="card" style="margin-top:12px;height:80px">
          <div class="row" style="gap:9px;align-items:flex-start"><div class="thumb" role="img" aria-label="Product photo" style="width:26px;height:26px;margin-top:2px"></div><div><div class="name" style="font-size:9px">Crisps selection</div><div class="sub" style="color:var(--text);margin-top:2px">3 bags of crisps</div></div></div>
          <div class="row" style="justify-content:flex-end;gap:8px;margin-top:8px"><div class="price">£5.00</div><div class="plus">+</div></div>
        </div>
        <div class="card" style="margin-top:10px;height:80px">
          <div class="row" style="gap:9px;align-items:flex-start"><div class="thumb" role="img" aria-label="Product photo" style="width:26px;height:26px;margin-top:2px"></div><div><div class="name" style="font-size:9px">2x TShirts</div><div class="sub" style="color:var(--text);margin-top:2px">Branded t-shirts</div></div></div>
          <div class="row" style="justify-content:flex-end;gap:8px;margin-top:8px"><div class="price">£25.00</div><div class="plus">+</div></div>
        </div>
      </div>
      <div class="btn" style="top:388px">Checkout £125.50</div>
      <div class="home-bar"></div>
    </section>

    <!-- Delivery details -->
    <section class="phone">
      <div class="status">9:41<div class="status-icons"><i></i><i></i><i class="bat"></i></div></div>
      <div class="head"><div class="back"><svg width="5" height="5" viewBox="0 0 6 6"><path d="M4 1L2 3l2 2" fill="none" stroke="#999" stroke-width=".7"/></svg></div><h2>Delivery details</h2></div>
      <div class="pad">
        <div style="position:relative;height:83px;margin-top:7px">
          <div role="img" aria-label="Street map around the delivery address" style="position:absolute;inset:0;border-radius:5px;background:linear-gradient(135deg,#E6E4E1 0 35%,#A8CF8A 35% 70%,#E6E4E1 70%)"></div>
          <div class="field" style="position:absolute;left:4px;right:4px;top:50px;background:#fff;border:none">
            <svg width="9" height="9" viewBox="0 0 10 10"><path d="M5 9.5S1.5 6 1.5 4a3.5 3.5 0 0 1 7 0C8.5 6 5 9.5 5 9.5z" fill="none" stroke="#A39E99" stroke-width=".8"/></svg>Your location</div>
        </div>
        <div class="label" style="margin-top:14px">Delivery date</div>
        <div class="field filled"><svg width="9" height="9" viewBox="0 0 10 10"><rect x="1" y="2" width="8" height="7" rx="1" fill="none" stroke="#A39E99" stroke-width=".8"/><path d="M1 4h8" stroke="#A39E99" stroke-width=".8"/></svg>01/01/2022</div>
        <div class="label" style="margin-top:12px">Name</div>
        <div class="field"><svg width="9" height="9" viewBox="0 0 10 10"><circle cx="5" cy="3.5" r="2" fill="none" stroke="#A39E99" stroke-width=".8"/><path d="M1.5 9a3.5 3.5 0 0 1 7 0" fill="none" stroke="#A39E99" stroke-width=".8"/></svg>Enter customer name</div>
        <div class="label" style="margin-top:12px">Email</div>
        <div class="field"><svg width="9" height="9" viewBox="0 0 10 10"><rect x="1" y="2.5" width="8" height="5.5" rx="1" fill="none" stroke="#A39E99" stroke-width=".8"/><path d="M1 3l4 3 4-3" fill="none" stroke="#A39E99" stroke-width=".8"/></svg>Enter customer email</div>
        <div class="label" style="margin-top:12px">Phone</div>
        <div class="field"><svg width="9" height="9" viewBox="0 0 10 10"><path d="M2 1.5l2 .5.5 2-1 1a5 5 0 0 0 2 2l1-1 2 .5.5 2C5 9 1 5 2 1.5z" fill="none" stroke="#A39E99" stroke-width=".8"/></svg>Enter phone number</div>
      </div>
      <div class="btn" style="top:388px">Proceed to pay £125.50</div>
      <div class="home-bar"></div>
    </section>

    <!-- Payment -->
    <section class="phone">
      <div class="status">9:41<div class="status-icons"><i></i><i></i><i class="bat"></i></div></div>
      <div class="head"><div class="back"><svg width="5" height="5" viewBox="0 0 6 6"><path d="M4 1L2 3l2 2" fill="none" stroke="#999" stroke-width=".7"/></svg></div><h2>Payment</h2></div>
      <div class="pad">
        <div class="check" style="margin-top:10px"><i></i>Stay updated on news and special offers.</div>
        <div class="check"><i></i>Share info with our brewer partners</div>
        <div class="label" style="margin-top:18px">Payment type selection</div>
        <div class="field select">Card Payment<span style="color:var(--muted)">⌄</span></div>
        <div style="background:var(--cream);border-radius:4px;padding:10px 9px;margin-top:12px">
          <div style="font-size:5.5px;color:var(--ink)">Card Details</div>
          <div class="field select" style="background:#fff;border:none;margin-top:6px">******7272<svg width="9" height="9" viewBox="0 0 10 10"><path d="M2 8l.5-2L7 1.5 8.5 3 4 7.5z M1 9h8" fill="none" stroke="#A39E99" stroke-width=".8"/></svg></div>
        </div>
        <p style="font-size:6.3px;color:var(--ink);margin-top:13px;line-height:1.7">By continuing to agree to our <b>T&amp;Cs</b>. Please also check out our <b>Privacy Policy</b>.</p>
        <div class="label" style="margin-top:12px">Delivery date</div>
        <div class="row" style="gap:8px;color:var(--text);font-size:7px"><svg width="9" height="9" viewBox="0 0 10 10"><rect x="1" y="2" width="8" height="7" rx="1" fill="none" stroke="#A39E99" stroke-width=".8"/><path d="M1 4h8" stroke="#A39E99" stroke-width=".8"/></svg>01/01/2022</div>
      </div>
      <div class="btn" style="top:388px">Proceed to pay £125.50</div>
      <div class="home-bar"></div>
    </section>

    <!-- Thank you -->
    <section class="phone">
      <div class="status">9:41<div class="status-icons"><i></i><i></i><i class="bat"></i></div></div>
      <h2 style="font-size:9.5px;font-weight:600;color:var(--ink);padding:18px 19px 0">Thank you...</h2>
      <div class="art" role="img" aria-label="Cartoon illustration of friends dancing and playing music under bunting" style="margin:30px 20px 0;height:110px"></div>
      <div class="pad" style="margin-top:16px">
        <p class="center-text">We have received your order. Get ready to party.</p>
        <p class="center-text" style="margin-top:6px">We will send you a confirmation email to <b>hello@barrelbay.test</b></p>
        <p class="center-text" style="margin-top:6px">You bought <b>Tallowmere brewery</b> beer. Go <span style="color:var(--orange)">learn more</span> about them.</p>
      </div>
      <div class="btn" style="top:388px">Buy more beer</div>
      <div class="home-bar"></div>
    </section>

    <!-- Oops -->
    <section class="phone">
      <div class="status">9:41<div class="status-icons"><i></i><i></i><i class="bat"></i></div></div>
      <div class="head"><div class="back"><svg width="5" height="5" viewBox="0 0 6 6"><path d="M4 1L2 3l2 2" fill="none" stroke="#999" stroke-width=".7"/></svg></div><h2>Oops...</h2></div>
      <div class="art" role="img" aria-label="Cartoon illustration of a confused traveller with a suitcase beside an oops sign" style="margin:40px 35px 0;height:110px"></div>
      <div class="pad" style="margin-top:22px">
        <p class="center-text">There was a problem processing your payment.</p>
        <p class="center-text" style="margin-top:6px">Please try again.</p>
      </div>
      <div class="home-bar"></div>
    </section>

    <!-- Marketplace home -->
    <section class="phone">
      <div class="status">9:41<div class="status-icons"><i></i><i></i><i class="bat"></i></div></div>
      <div class="row" style="gap:6px;padding-left:19px;margin-top:8px">
        <div class="photo" role="img" aria-label="Photo of a craft IPA can held in a hand" style="width:82px;height:82px;background:linear-gradient(160deg,#3C6D8A,#C9A04A 60%,#6B4A2A)"><span>IPAs</span></div>
        <div class="photo" role="img" aria-label="Photo of beer taps at a bar" style="width:82px;height:82px;background:linear-gradient(160deg,#2E4A66,#8A6A3E 60%,#3A2A1E)"><span>Lagers</span></div>
        <div class="photo" style="width:20px;height:82px;background:#3A6A8A"></div>
      </div>
      <div class="pad">
        <div class="section-label" style="margin-top:12px">Featured Breweries</div>
        <div class="row" style="gap:8px;margin-top:6px;width:200px">
          <div style="flex:none;width:137px">
            <div class="photo" role="img" aria-label="Photo of a row of poured beers in front of taps" style="width:137px;height:56px;background:linear-gradient(90deg,#C9862A,#E7B44C,#B8541E,#4A2A1E,#7A5A3A)"></div>
            <div style="font-size:6.3px;color:var(--ink);margin-top:2px">Tallowmere Brewery</div><div class="sub">London</div>
          </div>
          <div style="flex:none;width:40px">
            <div class="photo" role="img" aria-label="Brewery photo" style="width:40px;height:56px;background:linear-gradient(135deg,#3A2A1E,#8A6A3E)"></div>
            <div style="font-size:6.3px;color:var(--ink);margin-top:2px;white-space:nowrap">Local Brew</div><div class="sub">London</div>
          </div>
        </div>
        <div class="section-label" style="margin-top:10px">Popular beers</div>
        <div class="card" style="margin-top:7px">
          <div class="row" style="gap:9px;align-items:flex-start"><div class="thumb" role="img" aria-label="Tallowmere Brewery beer photo" style="width:48px;height:48px"></div><div><div class="name">Session IPA</div><div class="sub">Tallowmere Brewery</div><div class="stars">★★★<span>★★</span></div><div class="sub">5.2% Vol</div></div></div>
        </div>
      </div>
      <div class="btn" style="top:388px">View basket £125.50<span class="count">1</span></div>
      <div class="home-bar"></div>
    </section>

    <!-- IPAs list -->
    <section class="phone">
      <div class="status">9:41<div class="status-icons"><i></i><i></i><i class="bat"></i></div></div>
      <div class="head"><div class="back"><svg width="5" height="5" viewBox="0 0 6 6"><path d="M4 1L2 3l2 2" fill="none" stroke="#999" stroke-width=".7"/></svg></div><h2>IPAs</h2></div>
      <div class="pad">
        <div class="card" style="margin-top:12px"><div class="row" style="gap:9px;align-items:flex-start"><div class="thumb" role="img" aria-label="Tallowmere Brewery beer photo" style="width:48px;height:48px"></div><div><div class="name">Session IPA</div><div class="sub">Tallowmere Brewery</div><div class="stars">★★★<span>★★</span></div><div class="sub">5.2% Vol</div></div></div></div>
        <div class="card" style="margin-top:8px"><div class="row" style="gap:9px;align-items:flex-start"><div class="thumb" role="img" aria-label="Tallowmere Brewery beer photo" style="width:48px;height:48px"></div><div><div class="name">Session IPA</div><div class="sub">Tallowmere Brewery</div><div class="stars">★★★<span>★★</span></div><div class="sub">5.2% Vol</div></div></div></div>
        <div class="card" style="margin-top:8px"><div class="row" style="gap:9px;align-items:flex-start"><div class="thumb" role="img" aria-label="Tallowmere Brewery beer photo" style="width:48px;height:48px"></div><div><div class="name">Session IPA</div><div class="sub">Tallowmere Brewery</div><div class="stars">★★★<span>★★</span></div><div class="sub">5.2% Vol</div></div></div></div>
      </div>
      <div class="btn" style="top:388px">View basket £125.50<span class="count">1</span></div>
      <div class="home-bar"></div>
    </section>

    <!-- Beer detail -->
    <section class="phone">
      <div class="status">9:41<div class="status-icons"><i></i><i></i><i class="bat"></i></div></div>
      <div class="head"><div class="back"><svg width="5" height="5" viewBox="0 0 6 6"><path d="M4 1L2 3l2 2" fill="none" stroke="#999" stroke-width=".7"/></svg></div></div>
      <div class="pad">
        <div class="row" style="gap:9px;align-items:flex-start;margin-top:2px"><div class="thumb" role="img" aria-label="Tallowmere Brewery beer photo" style="width:48px;height:48px"></div><div><div class="name">Session IPA</div><div class="sub">Tallowmere Brewery</div><div class="stars">★★★<span>★★</span></div><div class="sub">5.2% Vol</div></div></div>
        <div class="card" style="margin-top:18px;height:50px;padding:10px 12px"><div class="row between"><div><div style="font-size:6.5px;color:var(--ink)">35 litres keg</div><div class="price" style="margin-top:2px">£65.00</div></div><div class="plus">+</div></div></div>
        <div class="card" style="margin-top:12px;height:50px;padding:10px 12px"><div class="row between"><div><div style="font-size:6.5px;color:var(--ink)">15 litres keg</div><div class="price" style="margin-top:2px">£45.00</div></div><div class="plus">+</div></div></div>
      </div>
      <div class="btn" style="top:388px">View basket £125.50<span class="count">1</span></div>
      <div class="home-bar"></div>
    </section>

    <!-- Brewery detail -->
    <section class="phone">
      <div class="status">9:41<div class="status-icons"><i></i><i></i><i class="bat"></i></div></div>
      <div class="head"><div class="back"><svg width="5" height="5" viewBox="0 0 6 6"><path d="M4 1L2 3l2 2" fill="none" stroke="#999" stroke-width=".7"/></svg></div></div>
      <div class="pad">
        <div class="orange-card" style="margin-top:2px">
          <div class="row" style="gap:7px"><div class="thumb" role="img" aria-label="Tallowmere Brewery photo" style="width:26px;height:26px"></div><div style="font-size:9px;font-weight:500;line-height:1.2">Tallowmere<br>Brewery</div></div>
          <p style="font-size:5.5px;margin-top:8px;line-height:1.6;color:#FFF0D8">Lorem ipsum dolor sit amet, consectetur adipiscing elit, sed do eiusmod tempor incididunt ut labore et dolore magna aliqua.</p>
        </div>
        <div class="card" style="margin-top:2px">
          <div class="name">Session IPA</div><div class="stars" style="margin-top:3px">★★★<span>★★</span></div><div class="sub">5.2% Vol</div>
          <p style="font-size:5.5px;color:var(--ink);margin-top:6px;line-height:1.6">Lorem ipsum dolor sit amet, consectetur adipiscing elit, sed do eiusmod tempor incididunt ut labore et dolore magna aliqua.</p>
        </div>
        <div class="card" style="margin-top:8px">
          <div class="name">Fruity IPA</div><div class="stars" style="margin-top:3px">★★★<span>★★</span></div><div class="sub">5.2% Vol</div>
          <p style="font-size:5.5px;color:var(--ink);margin-top:6px;line-height:1.6">Lorem ipsum dolor sit amet, consectetur adipiscing elit, sed do eiusmod tempor incididunt ut labore et dolore magna aliqua.</p>
        </div>
      </div>
      <div class="btn" style="top:388px">View basket £125.50<span class="count">1</span></div>
      <div class="home-bar"></div>
    </section>

  </div>
</main>
</body>
</html>
```